Quolvex custom business card design

Need a authentic, innovative business card design for a new mobile app business. I am uploading a few screen images from our app for you to view. I would like app design theme to match business card design. I can also send logo images.

```html
<!DOCTYPE html>
<html lang="en">
<head>
<meta charset="utf-8">
<title>Quolvex Business Card</title>
<link rel="stylesheet" href="https://fonts.googleapis.com/css2?family=Montserrat:wght@500;800&display=swap">
<style>
  :root {
    --brand-purple: #62038a;
    --ink: #1f1f1f;
    --paper: #ffffff;
    --faint-grey: #dedede;
    --faint-lilac: #e7d8ee;
    --shadow: rgba(0, 0, 0, 0.28);
  }
  * { margin: 0; padding: 0; box-sizing: border-box; }
  html, body {
    width: 1200px;
    height: 900px;
    overflow: hidden;
    background: var(--paper);
    font-family: "Montserrat", Arial, sans-serif;
  }
  .stage { position: relative; width: 1200px; height: 900px; }
  .card {
    position: absolute;
    left: 299px;
    width: 603px;
    height: 344px;
    overflow: hidden;
    box-shadow: 0 3px 10px var(--shadow);
  }
  .card--front { top: 81px; background: var(--brand-purple); }
  .card--back { top: 476px; background: var(--paper); }

  .brand-decor {
    position: absolute;
    left: 0;
    top: 0;
    height: 100%;
  }
  .card--front .brand-decor {
    width: 312px;
    background: linear-gradient(135deg, var(--ink) 0%, var(--ink) 30%, var(--paper) 30%, var(--paper) 100%);
  }
  .card--back .brand-decor {
    width: 300px;
    background: linear-gradient(160deg, var(--faint-grey) 0%, var(--paper) 55%, var(--faint-lilac) 100%);
  }

  .wordmark {
    position: absolute;
    display: flex;
    align-items: center;
    color: var(--ink);
    font-weight: 800;
    white-space: nowrap;
  }
  .wordmark__dot {
    border-radius: 50%;
    background: var(--brand-purple);
    flex: none;
  }
  .card--front .wordmark { left: 44px; top: 252px; font-size: 22px; gap: 8px; }
  .card--front .wordmark__dot { width: 14px; height: 14px; }
  .card--back .wordmark { left: 358px; top: 213px; font-size: 32px; gap: 10px; }
  .card--back .wordmark__dot { width: 20px; height: 20px; }

  .contact {
    position: absolute;
    left: 351px;
    top: 46px;
    width: 252px;
    color: var(--paper);
    font-weight: 500;
  }
  .contact__name { font-size: 21px; line-height: 26px; }
  .contact__title { font-size: 16px; line-height: 24px; }
  .contact__rule {
    height: 2px;
    background: var(--paper);
    margin: 10px 0 34px;
  }
  .contact__list { list-style: none; font-size: 16.5px; line-height: 25.5px; }
</style>
</head>
<body>
<main class="stage">
  <section class="card card--front" aria-label="Business card front">
    <div class="brand-decor" role="img" aria-label="Large brand symbol decoration"></div>
    <div class="wordmark"><span class="wordmark__dot"></span>Quolvex</div>
    <div class="contact">
      <p class="contact__name">Your Name</p>
      <p class="contact__title">Title</p>
      <div class="contact__rule"></div>
      <ul class="contact__list">
        <li>www.quolvex.com</li>
        <li>yourname@quolvex.com</li>
        <li>O: 021-555-0147</li>
        <li>F: 021-555-0147</li>
      </ul>
    </div>
  </section>

  <section class="card card--back" aria-label="Business card back">
    <div class="brand-decor" role="img" aria-label="Faint brand symbol decoration"></div>
    <div class="wordmark"><span class="wordmark__dot"></span>Quolvex</div>
  </section>
</main>
</body>
</html>
```